4 x Designs Required

Hi There,
I require 4 x different designs to be made for 4 new brands of mine however they can be quite interchangeable. HR Plinkr and Marketing Plinkr can be similar just with a difference in colour. The same goes for the Bulletin brands. This means there are ultimately two designs that need perfecting.

There must be a click here CTA on the banner somewhere. :-)

I require the banners in 728x90 format and 960x90 please.

Please use strap lines on the banners such as:
Essential Whitepapers for HR Professionals
Essential Whitepapers for Marketing Professionals
Your No.1 Whitepaper Resource

The brand names:
HR Plinkr
Marketing Plinkr
HR Dispatchly
Marketing Dispatchly

Examples attached.

```html
<!DOCTYPE html>
<html lang="en">
<head>
<meta charset="utf-8">
<title>Whitepaper Brand Banners</title>
<link rel="stylesheet" href="https://fonts.googleapis.com/css2?family=Arimo:wght@700&family=Exo+2:ital,wght@0,600;1,600&display=swap">
<style>
  :root {
    --page: #ffffff;
    --white: #ffffff;
    --orange: #f7981d;
    --orange-deep: #f97c14;
    --hr-navy: #0b2a78;
    --hr-navy-light: #2f62b4;
    --mk-purple: #5b0a9c;
    --mk-purple-light: #8a2cc0;
    --bul-indigo: #2a1488;
    --bul-indigo-light: #4a2cc8;
    --bul-red: #8e0a1c;
    --bul-red-light: #c0182c;
    --panel-dark: #2a282c;
  }
  * { box-sizing: border-box; margin: 0; padding: 0; }
  html, body {
    width: 1200px; height: 679px; overflow: hidden;
    background: var(--page);
  }
  .canvas { position: relative; width: 1200px; height: 679px; }

  .banner {
    position: absolute; left: 93px; width: 960px; height: 90px;
    overflow: hidden; color: var(--white);
  }
  .banner--hr-plinkr { top: 70px; background: var(--hr-navy); }
  .banner--mk-plinkr { top: 181px; background: var(--mk-purple); }
  .banner--hr-dispatchly { top: 380px; background: var(--bul-indigo); }
  .banner--mk-dispatchly { top: 486px; background: var(--bul-red); }

  /* Plinkr family */
  .skyline-photo {
    position: absolute; top: 0; right: 0; width: 380px; height: 90px;
  }
  .banner--hr-plinkr .skyline-photo {
    background: linear-gradient(90deg, rgba(11,42,120,0) 0%, rgba(47,98,180,0.85) 45%, #1c4a9a 75%, #3a78c4 100%);
  }
  .banner--mk-plinkr .skyline-photo {
    background: linear-gradient(90deg, rgba(91,10,156,0) 0%, rgba(138,44,192,0.85) 45%, #7a1cae 75%, #a040d8 100%);
  }
  .brand {
    position: absolute; top: 0; left: 32px; height: 90px;
    display: flex; align-items: center; gap: 10px;
  }
  .brand-dot {
    width: 40px; height: 40px; border-radius: 50%;
    background: var(--orange); flex: none;
  }
  .banner--mk-plinkr .brand-dot { background: var(--orange-deep); }
  .brand-name {
    font-family: "Arimo", Arial, sans-serif; font-weight: 700;
    font-size: 36px; line-height: 1; letter-spacing: -1px; color: var(--white);
  }
  .brand-name--stacked { font-size: 27px; line-height: 0.95; }
  .strapline {
    position: absolute; top: 0; height: 90px;
    display: flex; align-items: center;
    font-family: "Arimo", Arial, sans-serif; font-weight: 700;
    font-size: 21px; letter-spacing: -0.3px; white-space: nowrap;
  }
  .banner--hr-plinkr .strapline { left: 262px; }
  .banner--mk-plinkr .strapline { left: 249px; }
  .strapline-accent { color: var(--orange); margin-right: 6px; }
  .banner--mk-plinkr .strapline-accent { color: var(--orange-deep); }
  .cta-button {
    position: absolute; top: 25px; width: 158px; height: 43px;
    border-radius: 4px; background: var(--orange);
    display: flex; align-items: center; justify-content: center;
    font-family: "Arimo", Arial, sans-serif; font-weight: 700; font-size: 18px;
    color: var(--white); text-decoration: none;
  }
  .banner--hr-plinkr .cta-button { left: 756px; }
  .banner--mk-plinkr .cta-button { left: 787px; background: var(--orange-deep); }

  /* Dispatchly family */
  .hex-backdrop { position: absolute; inset: 0; }
  .banner--hr-dispatchly .hex-backdrop {
    background:
      radial-gradient(ellipse 260px 70px at 620px 60px, rgba(74,44,200,0.7), rgba(74,44,200,0) 70%),
      linear-gradient(90deg, #22106e 0%, var(--bul-indigo) 40%, var(--bul-indigo-light) 80%, #1a0c55 100%);
  }
  .banner--mk-dispatchly .hex-backdrop {
    background:
      radial-gradient(ellipse 260px 70px at 300px 20px, rgba(192,24,44,0.7), rgba(192,24,44,0) 70%),
      linear-gradient(90deg, var(--bul-red) 0%, var(--bul-red-light) 45%, #a8101f 75%, #7a0816 100%);
  }
  .bulletin-name {
    position: absolute; top: 0; height: 90px;
    display: flex; align-items: center;
    font-family: "Exo 2", "Trebuchet MS", sans-serif; font-weight: 600;
    color: var(--white); white-space: nowrap;
  }
  .banner--hr-dispatchly .bulletin-name { left: 54px; font-size: 38px; }
  .banner--mk-dispatchly .bulletin-name { left: 30px; font-size: 33px; }
  .bulletin-tagline {
    position: absolute; top: 0; left: 389px; height: 90px;
    display: flex; align-items: center;
    font-family: "Exo 2", "Trebuchet MS", sans-serif; font-style: italic; font-weight: 600;
    font-size: 22px; color: var(--white); white-space: nowrap;
  }
  .cta-panel { position: absolute; top: 0; left: 0; width: 960px; height: 90px; }
  .cta-panel path { fill: var(--panel-dark); }
  .cta-text {
    position: absolute; top: 0; left: 790px; width: 146px; height: 90px;
    display: flex; align-items: center; justify-content: center;
    font-family: "Arimo", Arial, sans-serif; font-weight: 700; font-size: 18px;
    color: var(--white); text-decoration: none;
  }
</style>
</head>
<body>
<main class="canvas">

  <section class="banner banner--hr-plinkr">
    <div class="skyline-photo" role="img" aria-label="Glass office tower facade photograph in blue tones"></div>
    <div class="brand">
      <span class="brand-dot"></span>
      <span class="brand-name">HR Plinkr</span>
    </div>
    <p class="strapline"><span class="strapline-accent">Essential Whitepapers</span>for HR Professionals</p>
    <a class="cta-button" href="#">CLICK HERE</a>
  </section>

  <section class="banner banner--mk-plinkr">
    <div class="skyline-photo" role="img" aria-label="Glass office tower facade photograph in purple tones"></div>
    <div class="brand">
      <span class="brand-dot"></span>
      <span class="brand-name brand-name--stacked">Marketing<br>Plinkr</span>
    </div>
    <p class="strapline"><span class="strapline-accent">Essential Whitepapers</span>for Marketing Professionals</p>
    <a class="cta-button" href="#">CLICK HERE</a>
  </section>

  <section class="banner banner--hr-dispatchly">
    <div class="hex-backdrop" role="img" aria-label="Glossy hexagonal tile backdrop in indigo tones"></div>
    <p class="bulletin-name">HR Dispatchly</p>
    <p class="bulletin-tagline">Your No.1 Whitepaper Resource</p>
    <svg class="cta-panel" viewBox="0 0 960 90" aria-hidden="true">
      <path d="M808 0 Q752 28 757 90 L960 90 L960 0 Z"/>
    </svg>
    <a class="cta-text" href="#">CLICK HERE</a>
  </section>

  <section class="banner banner--mk-dispatchly">
    <div class="hex-backdrop" role="img" aria-label="Glossy hexagonal tile backdrop in red tones"></div>
    <p class="bulletin-name">Marketing Dispatchly</p>
    <p class="bulletin-tagline">Your No.1 Whitepaper Resource</p>
    <svg class="cta-panel" viewBox="0 0 960 90" aria-hidden="true">
      <path d="M808 0 Q752 28 757 90 L960 90 L960 0 Z"/>
    </svg>
    <a class="cta-text" href="#">CLICK HERE</a>
  </section>

</main>
</body>
</html>
```